Vantor Ridge needs a Business Card Design

We need a business card design for an Information Technology company based in Fairfax Virginia called Vantor Ridge. We want the business card to use our logo colors. We need it to be double-sided. The business card needs to look professional but we would like it to be unique. You can get company information from our web site (http://www.vantorridgellc.example).

Target Market(s)

Target market is Government Agencies and Business Professionals.

Industry/Entity Type

Business

Requirements
Must have
• Must have section for company name, company address, company URL, employee name, title, phone and email. Also must have company logo and space for entering logos.

```html
<!DOCTYPE html>
<html lang="en">
<head>
<meta charset="utf-8">
<title>Vantor Ridge – Business Card</title>
<link rel="stylesheet" href="https://fonts.googleapis.com/css2?family=Carlito:wght@400;700&display=swap">
<style>
  :root {
    --backdrop: #e9eaec;
    --card-white: #ffffff;
    --brand-blue: #1450a3;
    --brand-navy: #1f3d86;
    --accent-blue: #2a6fc9;
    --text-grey: #7a7a7a;
    --frame-grey: #9a9a9a;
  }
  * { box-sizing: border-box; margin: 0; padding: 0; }
  html, body {
    width: 1200px; height: 900px; overflow: hidden;
    background: var(--backdrop);
    font-family: "Carlito", "Calibri", sans-serif;
  }
  .sheet {
    position: relative; width: 1200px; height: 900px;
    display: flex; align-items: center; justify-content: center; gap: 40px;
  }
  .card {
    position: relative; width: 520px; height: 300px;
    box-shadow: 0 6px 18px rgba(0,0,0,0.18);
  }

  /* Front */
  .card-front { background: var(--card-white); }
  .brand {
    position: absolute; left: 34px; top: 36px;
    display: flex; align-items: center; gap: 12px;
  }
  .brand-square { width: 30px; height: 30px; background: var(--brand-blue); }
  .brand-name {
    font-size: 30px; font-weight: 700; color: var(--brand-blue);
    letter-spacing: 0.3px;
  }
  .person { position: absolute; left: 34px; top: 132px; }
  .person-name { font-size: 20px; font-weight: 700; color: var(--brand-navy); }
  .person-title { font-size: 13px; font-weight: 700; color: var(--accent-blue); margin-top: 1px; }
  .address {
    position: absolute; left: 34px; top: 190px;
    font-size: 13px; line-height: 1.3; color: var(--text-grey);
  }
  .contact {
    position: absolute; left: 34px; top: 232px;
    list-style: none; font-size: 13px; color: var(--text-grey);
  }
  .contact li { display: flex; align-items: center; gap: 8px; height: 20px; }
  .contact svg { width: 14px; height: 14px; fill: var(--brand-navy); }
  .logo-slots {
    position: absolute; right: 30px; top: 112px;
    display: grid; grid-template-columns: repeat(4, 48px); gap: 6px;
  }
  .logo-slot { width: 48px; height: 42px; }
  .logo-slot rect, .logo-slot line { stroke: var(--frame-grey); stroke-width: 1; fill: none; }

  /* Back */
  .card-back {
    background: var(--brand-blue);
    display: flex; flex-direction: column; align-items: center; justify-content: center; gap: 18px;
  }
  .back-brand { display: flex; align-items: center; gap: 16px; }
  .back-square { width: 46px; height: 46px; background: var(--card-white); }
  .back-name { font-size: 46px; font-weight: 700; color: var(--card-white); }
  .back-url { font-size: 15px; color: var(--card-white); letter-spacing: 0.3px; }
</style>
</head>
<body>
<main class="sheet">

  <section class="card card-front" aria-label="Business card front">
    <div class="brand">
      <span class="brand-square"></span>
      <span class="brand-name">Vantor Ridge</span>
    </div>

    <div class="person">
      <p class="person-name">Employee Name</p>
      <p class="person-title">Employee title</p>
    </div>

    <address class="address" style="font-style:normal">
      4815 Harlow Ave, Suite 310<br>
      Fairfax, VA 22030
    </address>

    <ul class="contact">
      <li>
        <svg viewBox="0 0 14 14" aria-hidden="true"><path d="M3 1h6l1 2h2v10H2V3h1zM4 6h2v2H4zm3 0h2v2H7zM4 9h2v2H4zm3 0h2v2H7z" fill-rule="evenodd"/></svg>
        (800) 555 0142
      </li>
      <li>
        <svg viewBox="0 0 14 14" aria-hidden="true"><path d="M1 3h12v8H1zM2 4l5 4 5-4v-.2H2z" fill-rule="evenodd"/></svg>
        employee@vantorridgellc.example
      </li>
    </ul>

    <div class="logo-slots" aria-label="Space for partner logos">
      <svg class="logo-slot" viewBox="0 0 48 42"><rect x="0.5" y="0.5" width="47" height="41"/><line x1="0" y1="0" x2="48" y2="42"/><line x1="48" y1="0" x2="0" y2="42"/></svg>
      <svg class="logo-slot" viewBox="0 0 48 42"><rect x="0.5" y="0.5" width="47" height="41"/><line x1="0" y1="0" x2="48" y2="42"/><line x1="48" y1="0" x2="0" y2="42"/></svg>
      <svg class="logo-slot" viewBox="0 0 48 42"><rect x="0.5" y="0.5" width="47" height="41"/><line x1="0" y1="0" x2="48" y2="42"/><line x1="48" y1="0" x2="0" y2="42"/></svg>
      <svg class="logo-slot" viewBox="0 0 48 42"><rect x="0.5" y="0.5" width="47" height="41"/><line x1="0" y1="0" x2="48" y2="42"/><line x1="48" y1="0" x2="0" y2="42"/></svg>
      <svg class="logo-slot" viewBox="0 0 48 42"><rect x="0.5" y="0.5" width="47" height="41"/><line x1="0" y1="0" x2="48" y2="42"/><line x1="48" y1="0" x2="0" y2="42"/></svg>
      <svg class="logo-slot" viewBox="0 0 48 42"><rect x="0.5" y="0.5" width="47" height="41"/><line x1="0" y1="0" x2="48" y2="42"/><line x1="48" y1="0" x2="0" y2="42"/></svg>
      <svg class="logo-slot" viewBox="0 0 48 42"><rect x="0.5" y="0.5" width="47" height="41"/><line x1="0" y1="0" x2="48" y2="42"/><line x1="48" y1="0" x2="0" y2="42"/></svg>
      <svg class="logo-slot" viewBox="0 0 48 42"><rect x="0.5" y="0.5" width="47" height="41"/><line x1="0" y1="0" x2="48" y2="42"/><line x1="48" y1="0" x2="0" y2="42"/></svg>
    </div>
  </section>

  <section class="card card-back" aria-label="Business card back">
    <div class="back-brand">
      <span class="back-square"></span>
      <span class="back-name">Vantor Ridge</span>
    </div>
    <p class="back-url">www.vantorridgellc.example</p>
  </section>

</main>
</body>
</html>
```